DJ Marco Feng

I'm looking for a professional but still artsy/progressive design. I come from a hip hop/club DJ background playing a lot of underground music but have switched to doing more corporate parties and weddings recently. I am all about keeping the dancefloor moving and emotionally connecting with the crowd. I'd like a trendy/updated color palette. Something that's clean enough that looks professional but also trendy enough to convey that by the end of the night we'll be sweatily dancing to the latest hits. Some designers/artists I like: Tavi Rondquist, Niels Pardo, Clement Ruiz, Velvox 3100, Owen Tarbel.

```html
<!DOCTYPE html>
<html lang="en">
<head>
<meta charset="utf-8">
<title>DJ Business Card</title>
<link href="https://fonts.googleapis.com/css2?family=Arimo:wght@400&display=swap" rel="stylesheet">
<style>
  :root {
    --page-bg: #e9e6e1;
    --card-bg: #262626;
    --name-blue: #1c1ccf;
    --text-light: #f2f2f2;
    --card-shadow: rgba(0, 0, 0, 0.28);
  }
  html, body {
    margin: 0;
    width: 1200px;
    height: 900px;
    overflow: hidden;
    background: var(--page-bg);
    font-family: "Arimo", Arial, sans-serif;
  }
  .business-card {
    position: absolute;
    left: 100px;
    top: 164px;
    width: 1000px;
    height: 572px;
    background: var(--card-bg);
    box-shadow: 0 18px 40px var(--card-shadow);
    color: var(--text-light);
  }
  .brand {
    position: absolute;
    right: 40px;
    top: 38px;
    display: flex;
    flex-direction: column;
    align-items: center;
    gap: 14px;
  }
  .brand-mark {
    width: 70px;
    height: 70px;
    border-radius: 50%;
    background: var(--text-light);
  }
  .brand-name {
    font-size: 24px;
    letter-spacing: 0.5px;
    color: var(--text-light);
  }
  .identity {
    position: absolute;
    left: 46px;
    top: 318px;
  }
  .person-name {
    margin: 0;
    font-size: 36px;
    font-weight: 400;
    color: var(--name-blue);
    line-height: 1;
  }
  .person-role {
    margin: 4px 0 0;
    font-size: 14px;
    color: var(--text-light);
  }
  .contact {
    position: absolute;
    left: 46px;
    top: 420px;
    font-size: 20px;
    line-height: 1.2;
    font-style: normal;
  }
  .contact .web {
    font-size: 15px;
  }
</style>
</head>
<body>
  <section class="business-card">
    <div class="brand">
      <div class="brand-mark"></div>
      <div class="brand-name">YOUR COMPANY</div>
    </div>
    <div class="identity">
      <h1 class="person-name">John Doe</h1>
      <p class="person-role">Dj</p>
    </div>
    <address class="contact">
      <div class="phone">913-555-0147</div>
      <div class="street">Sample Address Street 1</div>
      <div class="street">Sample Address Street 2</div>
      <div class="web">www.yourcompany.com</div>
    </address>
  </section>
</body>
</html>
```